New solo practice law firm is looking for an elegant, professional, and interactive web design

I need a web design and developer for a new small law firm in Sacramento, California called Dorian Kessly Law, A Professional Corporation. I am a trial lawyer who represents average people facing difficult litigation disputes, including criminal defense as a former prosecutor and civil litigation as a civil litigator. Criminal defense includes domestic violence, battery, assault, drug possession, theft, DUI, etc. Civil litigation includes business disputes, property disputes, employment disputes, family law disputes, and immigration issues. I would like to see web designs that incorporate my logo and use the logo's navy blue and gold colors. I have uploaded the files of my logo to this brief. Please only use the navy blue and gold version. Overall, I want the design to look firm, professional, and elegant.

I plan on having the following pages on my website: (1) Home, (2) Dorian Kessly, (3) Practice Areas, (4) Insights, (5) Contact. I've hand drawn a preliminary sketch concept of what I envision the home page's layout to look like (attached with a text version). I would like your design to keep a similar layout for the homepage and incorporate my logo's colors within it but I am open to creative layout alternatives/ideas. I would like the other pages to have a similar look and feel as the home page. Some of the areas currently in my sketch do not have the full text. You can insert other text for now and I will provide the winner the full text.

In terms of the pictures on the website, I enjoy images of courthouses, columns (example attached but I cannot use this one), and, if possible, images from Sacramento, CA in my background (headshot attached). A plus would be live images that move and also sections of the webpage moving in the viewers view as they scroll down on the page. Also, it would be great to have my logo act as the tab for the website. I can provide other versions of the logo if needed.

I look forward to seeing your Wordpress designs!

People needing legal representation.

Law

Coded - Design and coding required

5+ page

Serif

• Incorporate my logo and my logo's colors.
• Live pictures and images appearing as viewers scroll on page.

```html
<!DOCTYPE html>
<html lang="en">
<head>
<meta charset="utf-8">
<title>About – Dorian Kessly Law</title>
<link href="https://fonts.googleapis.com/css2?family=Montserrat:wght@400;500;600;700&display=swap" rel="stylesheet">
<style>
:root{
  --navy:#172544;
  --navy-deep:#13203a;
  --gold:#c3a165;
  --gold-light:#dcc293;
  --gold-dark:#a07f45;
  --cream:#f6efdf;
  --ink:#1b2540;
  --text:#6b6f7a;
  --white:#ffffff;
}
*{margin:0;padding:0;box-sizing:border-box}
html,body{width:1200px;height:3145px;overflow:hidden}
body{position:relative;background:var(--white);font-family:"Montserrat",sans-serif;color:var(--ink)}
.abs{position:absolute}
.gold-grad{background:linear-gradient(90deg,var(--gold-light),var(--gold) 45%,var(--gold-dark))}

/* header */
.brand{left:125px;top:30px;display:flex;align-items:center;gap:8px}
.brand-mark{width:14px;height:14px;background:var(--gold);flex:none}
.brand-name{font-size:9px;line-height:12px;font-weight:600;color:var(--gold);letter-spacing:.08em}
.lang{left:240px;top:30px;width:144px;height:40px;border-radius:20px;background:#f1f1f3;display:flex;align-items:center;padding:0 14px;gap:10px;font-size:11px;color:#7a7f8a}
.lang .chev{margin-left:auto}
.head-icon{width:52px;height:52px;border-radius:50%;border:1.5px solid var(--gold-light);display:flex;align-items:center;justify-content:center}
.head-label{font-size:11px;font-weight:700;color:var(--ink)}
.head-small{font-size:9.5px;color:var(--text);line-height:15px;width:240px;margin-top:3px}
.head-phone{font-size:21px;color:var(--gold);margin-top:2px;letter-spacing:.02em}

.nav{left:125px;top:98px;width:950px;height:42px;display:flex;align-items:center;justify-content:space-around;z-index:3}
.nav a{font-size:9.5px;font-weight:700;letter-spacing:.28em;color:var(--white);text-decoration:none;position:relative}
.nav a.active::after{content:"";position:absolute;left:0;right:0;bottom:-15px;height:2px;background:var(--white)}
.nav .sep{width:4px;height:4px;border-radius:50%;background:var(--navy)}

/* hero */
.hero-photo{left:0;top:120px;width:1200px;height:370px;background:linear-gradient(90deg,#3b3a36 0%,#5a5548 30%,#2a3350 60%,#1b2a4d 100%)}
.hero-title{left:0;top:240px;width:1200px;text-align:center;font-size:46px;font-weight:500;letter-spacing:.3em;color:var(--white)}
.hero-dot{left:597px;top:360px;width:6px;height:6px;border-radius:50%;background:var(--white)}

/* about */
.about-kicker{left:125px;top:603px;font-size:26px;font-weight:500;letter-spacing:.2em}
.about-name{left:125px;top:632px;font-size:54px;font-weight:700;letter-spacing:.2em}
.ring{width:9px;height:9px;border-radius:50%;border:1.5px solid var(--gold)}
.copy{font-size:11.5px;line-height:21px;color:var(--text)}
.social-dot{width:32px;height:32px;border-radius:50%;background:#1769b3}
.signature{left:428px;top:968px;width:156px;height:72px;background:linear-gradient(135deg,rgba(120,120,130,.10),rgba(120,120,130,.22));border-radius:6px}
.portrait{left:650px;top:500px;width:460px;height:640px;background:linear-gradient(180deg,#d8b59a 0%,#b88c6e 30%,#2b2b30 55%,#141418 100%);border-radius:8px 8px 0 0}
.pattern{left:960px;top:420px;width:240px;height:260px;background:radial-gradient(circle,rgba(195,161,101,.10),rgba(255,255,255,0) 70%)}

/* what we do */
.wwd-title{left:0;top:1233px;width:1200px;text-align:center;font-size:26px;font-weight:600;letter-spacing:.22em;color:var(--white)}
.wwd-copy{left:220px;top:1290px;width:760px;text-align:center;font-size:11.5px;line-height:21px;color:#e6e8ee}
.stat-icon{width:70px;height:70px;border-radius:50%;background:rgba(255,255,255,.14);display:flex;align-items:center;justify-content:center}
.stat-num{font-size:58px;font-weight:500;color:var(--white);line-height:1}
.stat-label{font-size:10.5px;color:#e6e8ee;margin-top:8px;letter-spacing:.02em}

/* consultation */
.cream{left:0;top:1633px;width:1200px;height:1060px;background:var(--cream)}
.sched-kicker{left:0;top:1735px;width:1200px;text-align:center;font-size:26px;font-weight:500;letter-spacing:.24em}
.sched-title{left:0;top:1766px;width:1200px;text-align:center;font-size:54px;font-weight:700;letter-spacing:.2em}
.sched-copy{left:215px;top:1851px;width:770px;text-align:center;font-size:11.5px;line-height:21px;color:var(--text)}
.field{left:287px;width:626px;height:42px;background:var(--white);border-bottom:2px solid #f1e6cf;font-size:10px;color:#b3b5bb;padding:14px 22px}
.field.area{height:265px}
.cta{left:467px;top:2410px;width:266px;height:42px;display:flex;align-items:center;justify-content:center;gap:14px;font-size:9.5px;font-weight:700;letter-spacing:.28em;color:var(--white)}

/* footer */
.footer-bg{left:0;top:2600px;width:1200px;height:545px;background:var(--navy-deep)}
.f-title{font-size:17px;font-weight:600;letter-spacing:.22em;color:var(--white)}
.f-links{left:193px;top:2766px;width:170px;text-align:right;font-size:11.5px;line-height:30px;color:#dfe2ea}
.f-divider{width:1px;height:220px;background:rgba(255,255,255,.15)}
.f-brand{left:413px;top:2862px;width:372px;text-align:center}
.f-brand-name{font-size:17px;font-weight:500;letter-spacing:.14em;color:var(--gold)}
.f-brand-sub{font-size:7.5px;letter-spacing:.24em;color:var(--gold);margin-top:6px}
.f-mark{left:583px;top:2745px;width:34px;height:34px;border:2px solid var(--gold)}
.f-contact{left:838px;top:2766px;width:220px;font-size:10.5px;line-height:18px;color:#c9cdd8}
.f-contact b{color:var(--white);font-weight:700}
.f-rule{left:125px;top:2968px;width:950px;height:1px;background:rgba(255,255,255,.14)}
.f-legal{left:190px;top:2990px;width:820px;text-align:center;font-size:9.5px;line-height:16px;color:#c9cdd8}
.f-copy{left:0;top:3038px;width:1200px;text-align:center;font-size:9.5px;color:#c9cdd8}
.f-social{width:32px;height:32px;border-radius:50%}
.chat{left:1086px;top:3032px;width:72px;height:72px;border-radius:50%;display:flex;align-items:center;justify-content:center;box-shadow:0 6px 18px rgba(0,0,0,.3)}
</style>
</head>
<body>

<header>
  <div class="abs brand"><span class="brand-mark"></span><span class="brand-name">DORIAN KESSLY<br>LAW</span></div>
  <div class="abs lang">
    <svg width="14" height="14" viewBox="0 0 24 24" fill="none" stroke="#555" stroke-width="1.6"><circle cx="12" cy="12" r="9"/><path d="M3 12h18M12 3c3 3.5 3 14.5 0 18M12 3c-3 3.5-3 14.5 0 18"/></svg>
    English
    <svg class="chev" width="12" height="12" viewBox="0 0 24 24" fill="none" stroke="#555" stroke-width="2"><path d="M6 9l6 6 6-6"/></svg>
  </div>
  <div class="abs head-icon" style="left:459px;top:21px">
    <svg width="20" height="20" viewBox="0 0 24 24" fill="none" stroke="#1b2540" stroke-width="1.6"><path d="M12 22s7-7 7-12a7 7 0 0 0-14 0c0 5 7 12 7 12z"/><circle cx="12" cy="10" r="2.5"/></svg>
  </div>
  <div class="abs" style="left:530px;top:25px">
    <div class="head-label">Location:</div>
    <div class="head-small">Lorem Ipsum is simply dummy text of the printing and typesetting industry.</div>
  </div>
  <div class="abs head-icon" style="left:842px;top:21px">
    <svg width="20" height="20" viewBox="0 0 24 24" fill="none" stroke="#1b2540" stroke-width="1.6"><path d="M5 3h4l2 5-2.5 1.5a11 11 0 0 0 6 6L16 13l5 2v4a2 2 0 0 1-2 2A17 17 0 0 1 3 5a2 2 0 0 1 2-2z"/></svg>
  </div>
  <div class="abs" style="left:913px;top:25px">
    <div class="head-label">Free Consultation:</div>
    <div class="head-phone">(916) 555-0148</div>
  </div>
</header>

<div class="abs hero-photo" role="img" aria-label="Photo of a domed capitol building with columns, darkened in navy tones"></div>
<nav class="abs nav gold-grad">
  <a href="#">HOME</a><span class="sep"></span>
  <a href="#" class="active">DORIAN KESSLY</a><span class="sep"></span>
  <a href="#">PRACTICE AREAS</a><span class="sep"></span>
  <a href="#">INSIGHTS</a><span class="sep"></span>
  <a href="#">CONTACT</a>
</nav>
<h1 class="abs hero-title">ABOUT</h1>
<div class="abs hero-dot"></div>
<svg class="abs" style="left:0;top:395px" width="1200" height="100" viewBox="0 0 1200 100">
  <defs><linearGradient id="g1" x1="0" x2="1"><stop offset="0" stop-color="#dcc293"/><stop offset=".5" stop-color="#c3a165"/><stop offset="1" stop-color="#a07f45"/></linearGradient></defs>
  <polygon points="0,13 190,88 1200,0 1200,100 0,100" fill="url(#g1)"/>
  <polygon points="0,13 190,78 1200,18 1200,100 0,100" fill="#ffffff"/>
</svg>

<section>
  <div class="abs pattern" role="img" aria-label="Faint geometric line pattern"></div>
  <h2 class="abs about-kicker">ABOUT DORIAN</h2>
  <div class="abs about-name">KESSLY</div>
  <div class="abs ring" style="left:440px;top:662px"></div>
  <p class="abs copy" style="left:125px;top:718px;width:460px">Lorem Ipsum is simply dummy text of the printing and typesetting industry. Lorem Ipsum has been the industry's standard dummy text ever since the 1500s, when an unknown printer took a galley of type and scrambled it to make a type specimen book. It has survived not only five centuries, but also the leap into electronic typesetting, remaining essentially unchanged. It was popularised in the 1960s with the release of Letraset sheets.</p>
  <p class="abs copy" style="left:125px;top:885px;width:460px">Lorem Ipsum is simply dummy text of the printing and typesetting industry. Lorem Ipsum has been the industry's standard dummy text ever since the 1500s, when an unknown printer took a galley of type and scrambled it to make a type specimen book.</p>
  <div class="abs social-dot" style="left:126px;top:1009px" role="img" aria-label="Professional network profile"></div>
  <div class="abs signature" role="img" aria-label="Handwritten signature of Dorian Kessly"></div>
  <div class="abs portrait" role="img" aria-label="Portrait of attorney Dorian Kessly in a dark suit and tie"></div>
</section>

<section>
  <svg class="abs" style="left:0;top:1095px" width="1200" height="545" viewBox="0 0 1200 545">
    <defs><linearGradient id="g2" x1="0" x2="1"><stop offset="0" stop-color="#dcc293"/><stop offset="1" stop-color="#a07f45"/></linearGradient>
    <linearGradient id="nv" x1="0" y1="0" x2="0" y2="1"><stop offset="0" stop-color="#1d2d52"/><stop offset="1" stop-color="#1a2a4c"/></linearGradient></defs>
    <polygon points="640,35 1010,8 1200,75 1200,40 1010,2" fill="url(#g2)"/>
    <polygon points="0,83 1010,10 1200,75 1200,545 0,545" fill="url(#nv)" role="img" aria-label="Navy-toned photo of courthouse columns and steps"/>
  </svg>
  <h2 class="abs wwd-title">WHAT WE DO</h2>
  <p class="abs wwd-copy">Lorem Ipsum is simply dummy text of the printing and typesetting industry. Lorem Ipsum has been the industry's standard dummy text ever since the 1500s, when an unknown printer took a galley of type and scrambled it to make a type specimen book. It has survived not only five centuries, but also the leap into electronic typesetting, remaining essentially unchanged. It was popularised in the 1960s with the release of Letraset sheets.</p>

  <div class="abs stat-icon" style="left:153px;top:1430px">
    <svg width="28" height="28" viewBox="0 0 24 24" fill="#dcc293"><circle cx="12" cy="8" r="3"/><circle cx="5.5" cy="10" r="2.2"/><circle cx="18.5" cy="10" r="2.2"/><path d="M6.5 19c0-3.5 2.5-6 5.5-6s5.5 2.5 5.5 6z"/><path d="M1.5 19c0-2.7 1.8-4.5 4-4.5 1 0 1.6.3 2.2.7A7 7 0 0 0 5.2 19zM22.5 19c0-2.7-1.8-4.5-4-4.5-1 0-1.6.3-2.2.7a7 7 0 0 1 2.5 3.8z"/></svg>
  </div>
  <div class="abs" style="left:248px;top:1432px"><div class="stat-num">206+</div><div class="stat-label">LAWYERS TEAM</div></div>

  <div class="abs stat-icon" style="left:497px;top:1430px">
    <svg width="28" height="28" viewBox="0 0 24 24" fill="none" stroke="#dcc293" stroke-width="1.8"><circle cx="12" cy="9" r="6"/><circle cx="12" cy="9" r="2.5"/><path d="M8.5 14l-2 7 5.5-3 5.5 3-2-7"/></svg>
  </div>
  <div class="abs" style="left:592px;top:1432px"><div class="stat-num">95+</div><div class="stat-label">CASES WE WON</div></div>

  <div class="abs stat-icon" style="left:800px;top:1430px">
    <svg width="28" height="28" viewBox="0 0 24 24" fill="#dcc293"><path d="M4 4h4l2 5-2.5 1.5a11 11 0 0 0 6 6L15 14l5 2v4a1.5 1.5 0 0 1-1.5 1.5A17 17 0 0 1 2.5 5.5 1.5 1.5 0 0 1 4 4z"/><circle cx="17.5" cy="6.5" r="4.5"/></svg>
  </div>
  <div class="abs" style="left:895px;top:1432px"><div class="stat-num">524+</div><div class="stat-label">FREE CONSULTATIONS</div></div>
</section>

<section>
  <div class="abs cream"></div>
  <div class="abs pattern" style="top:1633px;left:940px;width:260px;height:240px" role="img" aria-label="Faint geometric line pattern"></div>
  <div class="abs pattern" style="top:2420px;left:0;width:260px;height:240px" role="img" aria-label="Faint geometric line pattern"></div>
  <h2 class="abs sched-kicker">SCHEDULE A FREE</h2>
  <div class="abs sched-title">CONSULTATION</div>
  <div class="abs ring" style="left:277px;top:1795px"></div>
  <div class="abs ring" style="left:914px;top:1795px"></div>
  <p class="abs sched-copy">Lorem Ipsum is simply dummy text of the printing and typesetting industry. Lorem Ipsum has been the industry's standard dummy text ever since the 1500s, when an unknown printer took a galley of type and scrambled it to make a type specimen book. It has survived not only five centuries, but also the leap into electronic typesetting.</p>
  <div class="abs" style="left:327px;top:2430px;width:546px;height:60px;background:rgba(200,180,140,.12)"></div>
  <div class="abs field" style="top:1963px">Your Name</div>
  <div class="abs field" style="top:2011px">Email address</div>
  <div class="abs field" style="top:2060px">Phone no.</div>
  <div class="abs field" style="top:2108px">Select service</div>
  <div class="abs field area" style="top:2158px">Type your message...</div>
  <div class="abs cta gold-grad">GET A CONSULTATION
    <svg width="10" height="10" viewBox="0 0 24 24" fill="none" stroke="#fff" stroke-width="3"><path d="M9 5l7 7-7 7"/></svg>
  </div>
</section>

<footer>
  <svg class="abs" style="left:0;top:2585px" width="1200" height="90" viewBox="0 0 1200 90">
    <defs><linearGradient id="g3" x1="0" x2="1"><stop offset="0" stop-color="#dcc293"/><stop offset="1" stop-color="#a07f45"/></linearGradient></defs>
    <polygon points="640,45 1008,5 1200,60 1200,78 1008,14" fill="url(#g3)"/>
    <polygon points="0,78 1008,14 1200,78 1200,90 0,90" fill="#13203a"/>
  </svg>
  <div class="abs footer-bg" style="top:2660px;height:485px"></div>

  <h3 class="abs f-title" style="left:193px;top:2717px">QUICK LINKS</h3>
  <div class="abs f-links">Home<br>Dorian Kessly<br>Practice Areas<br>Insights<br>Contact</div>
  <div class="abs f-divider" style="left:413px;top:2700px"></div>

  <div class="abs f-mark"></div>
  <div class="abs f-brand">
    <div class="f-brand-name">DORIAN KESSLY LAW</div>
    <div class="f-brand-sub">A PROFESSIONAL CORPORATION</div>
  </div>

  <div class="abs f-divider" style="left:785px;top:2700px"></div>
  <h3 class="abs f-title" style="left:838px;top:2717px">CONTACT INFO</h3>
  <div class="abs f-contact">
    <b>Location:</b><br>Lorem Ipsum is simply dummy<br>text of the printing<br><br>
    <b>Call:</b><br>(916) 555-0148
  </div>

  <div class="abs f-rule"></div>
  <p class="abs f-legal">The information on this website is for general information purpose only. Nothing on this site should be taken as legal advice for any individual case or situtation. This information is not intended to create, and recipt or including does not constitute, an attorney-client relationship.</p>
  <p class="abs f-copy">© 2021 Dorian Kessly Law Inc. All right reserved.</p>

  <div class="abs f-social" style="left:541px;top:3074px;background:#3a5a9e" role="img" aria-label="Social profile"></div>
  <div class="abs f-social" style="left:584px;top:3074px;background:#1769b3" role="img" aria-label="Social profile"></div>
  <div class="abs f-social" style="left:627px;top:3074px;background:#3fa6e6" role="img" aria-label="Social profile"></div>

  <div class="abs chat gold-grad">
    <svg width="30" height="30" viewBox="0 0 24 24" fill="none" stroke="#fff" stroke-width="1.8"><path d="M4 5h16v11H9l-4 4v-4H4z"/><path d="M8 10.5h.01M12 10.5h.01M16 10.5h.01" stroke-width="2.6" stroke-linecap="round"/></svg>
  </div>
</footer>

</body>
</html>
```